Halvorn Hire Business Card Design

Need business cards designed for our new equipment rental. We specialize in renting to landscape / tree professionals, contractors, Do-It-Yourself'ers and Around the home or office. Looking for a eye catching card. Landscape and construction should be the theme. The logo is attached, and you can see our colors from the logo. You can use whatever color goes with it ok.

Target Market(s)

First off Landscape and Tree Professional. Then contractors, Do-It-Yourself'ers and rentals for Around the home or office.

Industry/Entity Type

Business

Contact Information for Business Card

Eye catching background that blends landscaping with construction equipment

Requirements
Must have
• Name on Card will Be: Derek Pollard (Manager)
• My Direct Phone Number is: 555-418-7093
• derek@halvornhire.example
• www.halvornhire.example
• 4172 Wexley Mill Road,
• Marrow Vale ZZ 00590
Nice to have
• Would be Nice to have these bullets on the Face of the card that does not have all my information.
• Serving:
• Landscape / Tree Professionals
• Contractors
• DYI'ers or say Do-It-Yourself'ers
• Maybe have serving small and centered above these bullets, and these 3 bullets along the bottom of the card. Ideas?

```html
<!DOCTYPE html>
<html lang="en">
<head>
<meta charset="utf-8">
<title>Halvorn Hire Business Card</title>
<link href="https://fonts.googleapis.com/css2?family=Lato:wght@400;700;900&display=swap" rel="stylesheet">
<style>
  :root{
    --page:#e9e6e1;
    --blue:#0e5fa3;
    --blue-deep:#0a3e72;
    --navy:#17508f;
    --gold:#f3c56f;
    --grey:#c4c6c8;
    --white:#ffffff;
    --paper:#f7f7f7;
  }
  *{box-sizing:border-box;margin:0;padding:0}
  html,body{width:1200px;height:780px;overflow:hidden}
  body{background:var(--page);font-family:"Lato",sans-serif;display:flex;align-items:center;justify-content:center;gap:40px}
  .card{position:relative;width:560px;height:320px;border-radius:4px;overflow:hidden;box-shadow:0 10px 28px rgba(0,0,0,.18)}
  .card-front{background:var(--paper)}
  .front-shape{position:absolute;inset:0}
  .brand{position:absolute;display:flex;align-items:center;gap:10px;font-weight:900;text-transform:uppercase;letter-spacing:1px;white-space:nowrap}
  .brand-mark{width:14px;height:14px;background:currentColor;flex:none}
  .card-front .brand{left:38px;top:200px;color:var(--navy);font-size:24px}
  .details{position:absolute;left:318px;top:34px;color:var(--white)}
  .name{font-weight:900;font-size:19px;text-transform:uppercase;letter-spacing:.3px}
  .role{color:var(--gold);font-size:12px;margin-top:2px}
  .contact{list-style:none;margin-top:14px;font-size:12.5px;line-height:1.55}
  .contact li{display:flex;align-items:center;gap:8px}
  .contact svg{width:15px;height:15px;flex:none}
  .address{font-size:12.5px;line-height:1.45;margin-top:4px;padding-left:23px}
  .serving-title{color:var(--gold);font-weight:700;font-size:15px;margin-top:16px}
  .serving{list-style:none;font-size:12.5px;line-height:1.5;margin-top:4px}
  .serving li{display:flex;align-items:center;gap:8px}
  .serving li::before{content:"";width:6px;height:6px;border-radius:50%;background:var(--gold);flex:none}
  .card-back{background:radial-gradient(ellipse at 40% 30%, var(--blue) 0%, var(--blue-deep) 100%)}
  .card-back .brand{left:0;right:0;top:130px;justify-content:center;color:var(--white);font-size:34px}
  .website{position:absolute;left:0;right:0;top:196px;text-align:center;color:var(--gold);font-size:14px;letter-spacing:2px;text-transform:uppercase}
</style>
</head>
<body>
  <section class="card card-front">
    <svg class="front-shape" viewBox="0 0 560 320" aria-hidden="true">
      <defs>
        <linearGradient id="frontBlue" x1="0" y1="0" x2="1" y2="1">
          <stop offset="0" stop-color="#1066ab"/>
          <stop offset="1" stop-color="#0a4379"/>
        </linearGradient>
      </defs>
      <path d="M236 0 H560 V320 H312 C244 236 330 96 236 0 Z" fill="#c4c6c8"/>
      <path d="M250 0 H560 V320 H326 C258 236 344 96 250 0 Z" fill="url(#frontBlue)"/>
    </svg>
    <div class="brand"><span class="brand-mark"></span>Halvorn Hire</div>
    <div class="details">
      <p class="name">Derek Pollard</p>
      <p class="role">Manager</p>
      <ul class="contact">
        <li><svg viewBox="0 0 16 16"><circle cx="8" cy="8" r="7" fill="none" stroke="#f3c56f" stroke-width="1.3"/><rect x="5.5" y="4" width="5" height="8" rx="1" fill="#f3c56f"/></svg>555-418-7093</li>
        <li><svg viewBox="0 0 16 16"><circle cx="8" cy="8" r="7" fill="none" stroke="#f3c56f" stroke-width="1.3"/><rect x="4" y="5" width="8" height="6" rx=".8" fill="#f3c56f"/><path d="M4.3 5.4 8 8.4 11.7 5.4" fill="none" stroke="#0e5fa3" stroke-width="1"/></svg>derek@halvornhire.example</li>
      </ul>
      <p class="address">4172 Wexley Mill Road,<br>Marrow Vale ZZ 00590</p>
      <p class="serving-title">Serving:</p>
      <ul class="serving">
        <li>Landscape / Tree Professionals</li>
        <li>Contractors</li>
        <li>DYI'ers or say Do-It-Yourself'ers</li>
      </ul>
    </div>
  </section>
  <section class="card card-back">
    <div class="brand"><span class="brand-mark"></span>Halvorn Hire</div>
    <p class="website">www.halvornhire.example</p>
  </section>
</body>
</html>
```